Catering Menu Package

I currently have a complete menu package, which we have redesigned as far as content, now I need to it put together in a catalog type format. It is essentially 10-12 pages in length, and will be sent for print production. Upon receiving a final edit
Updates

I have added an example gif to the project.

I did this free hand this basically what I am looking for. please change text and type to whatever you think would look best. This is a total rough design so, feel free to change any and everything. The text for the page is on the word documents. If you need more images let me know I am in the process of getting as many images uploaded for your use.

Reason: I figured we got a late jump with questions, so i am extending a few days .

Target Market(s)

The target market is business who wish to have catered luncheons, breakfasts , meetings

Industry/Entity Type

Catering

Requirements
Must have
• I have attached a copy of the text that what we want in the package, our logo, and i have also attached a catering package of another company to give you an idea what the finished product will be
Should not have
• It should not look identical to the example catering packages, these are for some inspiration we want our own design with the same type of look and feel

```html
<!DOCTYPE html>
<html lang="en">
<head>
<meta charset="utf-8">
<title>Entrée Sides &amp; Fresh Salads — Briarwood Table Caterers</title>
<link rel="stylesheet" href="https://fonts.googleapis.com/css2?family=Parisienne&family=Lora:ital,wght@0,400;1,700&display=swap">
<style>
  :root {
    --page-bg: #f4f3f2;
    --panel-bg: #ffffff;
    --heading: #6e6561;
    --heading-shadow: rgba(90, 80, 75, 0.35);
    --body-text: #6a5548;
    --accent-green: #1f8657;
    --brand-ink: #1e1e1e;
    --brand-mark: #e06a1c;
  }
  * { margin: 0; padding: 0; box-sizing: border-box; }
  html, body { width: 1200px; height: 927px; overflow: hidden; }
  body {
    position: relative;
    background: linear-gradient(90deg, #ffffff 0%, var(--page-bg) 100%);
    font-family: "Lora", Georgia, serif;
    color: var(--body-text);
  }
  .menu-page { position: absolute; inset: 0; }
  .content-panel {
    position: absolute; left: 182px; top: 0; width: 1018px; height: 927px;
    background: linear-gradient(180deg, #fbfbfb 0%, var(--panel-bg) 30%, #f6f5f4 100%);
  }
  .left-margin {
    position: absolute; left: 0; top: 0; width: 182px; height: 927px;
    background: linear-gradient(90deg, #ffffff 0%, #efedec 100%);
  }

  .brand { position: absolute; left: 28px; top: 40px; width: 140px; text-align: center; }
  .brand-mark { width: 70px; height: 70px; margin: 0 auto 14px; background: var(--brand-mark); }
  .brand-name {
    font-family: "Lora", Georgia, serif; font-size: 21px; line-height: 1.15;
    color: var(--brand-ink); font-weight: 400;
  }

  .section-title {
    position: absolute; font-family: "Parisienne", cursive; font-weight: 400;
    font-size: 44px; color: var(--heading); white-space: nowrap;
    text-shadow: 2px 2px 3px var(--heading-shadow);
  }
  .title-sides { left: 197px; top: 40px; }
  .title-salads { left: 197px; top: 383px; }
  .title-vegetables { left: 689px; top: 292px; font-size: 40px; }

  .body-copy { position: absolute; font-size: 17px; line-height: 23px; }
  .sides-list { left: 197px; top: 126px; width: 460px; }
  .sides-list p + p { margin-top: 27px; }
  .price { margin-left: 14px; }

  .salad-list { left: 197px; top: 465px; width: 468px; }
  .salad-item + .salad-item { margin-top: 17px; }
  .salad-name {
    font-style: italic; font-weight: 700; color: var(--accent-green);
    font-size: 18px; line-height: 23px;
  }
  .salad-desc { font-size: 16px; line-height: 23px; }

  .vegetable-list { left: 692px; top: 379px; width: 400px; list-style: none; }
  .vegetable-list li { font-size: 17px; line-height: 36.5px; }

  .photo { position: absolute; }
  .photo-baguettes { left: 664px; top: 29px; width: 136px; height: 191px;
    background: linear-gradient(160deg, #c9c6c3 0%, #d8a868 45%, #a87a44 100%); }
  .photo-green-salad { left: 808px; top: 35px; width: 129px; height: 180px;
    background: linear-gradient(150deg, #a0524a 0%, #4d8a3c 45%, #2d5f9a 100%); }
  .photo-rolls { left: 944px; top: 38px; width: 256px; height: 174px;
    background: radial-gradient(ellipse at 45% 45%, #e4b76a 0%, #cf9a4c 45%, #ece7df 100%); }
  .photo-salad-plate { left: 330px; top: 247px; width: 336px; height: 152px;
    border-radius: 50%;
    background: radial-gradient(ellipse at 50% 45%, #8fbf4a 0%, #c7a46a 45%, #e6e3b0 70%, rgba(255,255,255,0) 72%); }
  .photo-vegetables { left: 682px; top: 652px; width: 518px; height: 275px;
    border-radius: 60% 0 0 0 / 40% 0 0 0;
    background: linear-gradient(200deg, #4a8a2a 0%, #6aa83a 40%, #f08a2a 62%, #f3801c 100%); }
</style>
</head>
<body>
<main class="menu-page">
  <div class="left-margin"></div>
  <div class="content-panel"></div>

  <header class="brand">
    <div class="brand-mark"></div>
    <p class="brand-name">Briarwood<br>Table<br>Caterers</p>
  </header>

  <h2 class="section-title title-sides">Entrée Sides</h2>
  <div class="body-copy sides-list">
    <p>Fresh House Baked Rolls &amp; Artisan Baguettes with<br>Whipped Butter<span class="price">$&amp;.&amp;&amp; Per Dozen</span></p>
    <p>Fresh Baked Garlic Bread<span class="price">$&amp;.&amp;&amp; Per Dozen</span></p>
  </div>

  <div class="photo photo-baguettes" role="img" aria-label="Artisan baguettes on a grey background"></div>
  <div class="photo photo-green-salad" role="img" aria-label="Green leaf salad on a blue plate"></div>
  <div class="photo photo-rolls" role="img" aria-label="Basket of golden baked dinner rolls"></div>
  <div class="photo photo-salad-plate" role="img" aria-label="Plate of salad with sliced grilled chicken and a fork"></div>

  <h2 class="section-title title-salads">Fresh Salads</h2>
  <div class="body-copy salad-list">
    <section class="salad-item">
      <h3 class="salad-name">Tropical Salad</h3>
      <p class="salad-desc">Customer Favorite! Spring Mix, Feta Cheese, Mandarin<br>Oranges, &amp; Craisins.Served with our Fat-Free Raspberry<br>Vinaigrette.</p>
    </section>
    <section class="salad-item">
      <h3 class="salad-name">Classic Caesar Salad</h3>
      <p class="salad-desc">Crisp Romaine Lettuce, Creamy Caesar Dressing, Garlic<br>Croutons, &amp; Imported Parmsan Cheese.</p>
    </section>
    <section class="salad-item">
      <h3 class="salad-name">Roman Salad</h3>
      <p class="salad-desc">Crisp Romaine Lettuce, Black Olives, Grape Tomatoes,<br>Feta Cheese, &amp; Red Onions.Served with our Chef-made<br>Parmesan-Pepper Dressing.</p>
    </section>
    <section class="salad-item">
      <h3 class="salad-name">Farm Fresh Garden Salad</h3>
      <p class="salad-desc">Spring Mix, Shredded Carrots, Grape Tomatoes, Cucum-<br>bers, Red Onions, &amp; Garlic Croutons.Accompanied with<br>Ranch Dressing &amp; our Chef-made Balsamic Dressing.</p>
    </section>
  </div>

  <h2 class="section-title title-vegetables">Vegetable Substitutes</h2>
  <ul class="body-copy vegetable-list">
    <li>To substitute, free of charge, to add $&amp;.&amp;&amp;</li>
    <li>Lemon Scented Petit Green Beans</li>
    <li>Tomato-Zucchini Casserole</li>
    <li>Steamed Broccoli</li>
    <li>Maple Glazed Carrots</li>
    <li>Sautéed Local Corn</li>
  </ul>

  <div class="photo photo-vegetables" role="img" aria-label="Baby carrots and steamed broccoli florets"></div>
</main>
</body>
</html>
```